Premium Gold Vodka Label Design

English ------------------- We need a label for a Vodka Bottle. Its a sparkling premium vodka with gold inside. The design should look premium. We tried it on our selves but it looks horrible. Therefore we need your help. The current name is corvelle K, but we are open for any better suggestion. We attached the selfmade design. The label will be printed on the bottle. We have other design jobs for you (logo, other sorts)! English ------------------------ We need a label for a vodka bottle. This is a premium vodka which is offset with gold. The design should look like this. We have tried so far and failed. That is why we need your support. The name is so far corvelle K. If you have better suggestions we would be pleased about other suggestions / ideas. In the appendix the failed design is stored. The label is to be applied by screen printing. In the case of good work follow-up projects are guaranteed (logo, other varieties, etc)!
Updates

Reason: We need more time for the decision.

Target Market(s)

USA

Colors

Designer to choose colors to be used in the design.

Requirements
Must have
• English ------------------------ The needed text is on our selfmade label that is attached. English ------------------------ The required texts are stored in the attached design.
Nice to have
• English ------------------------ Transparent places are allowed because we want to print the label on the bottom. English ------------------------ As the label is applied by screen printing, transparent areas are also possible.

```html
<!DOCTYPE html>
<html lang="en">
<head>
<meta charset="utf-8">
<title>Corvelle K — 24 kt Premium Gold Sparkling Vodka Labels</title>
<link rel="stylesheet" href="https://fonts.googleapis.com/css2?family=Cinzel:wght@400;700&family=Pinyon+Script&family=Tinos:wght@400;700&display=swap">
<style>
  :root {
    --canvas-top: #c4c4c4;
    --canvas-bottom: #ffffff;
    --label-black: #050505;
    --label-white: #ffffff;
    --gold: #c9a04a;
    --gold-dark: #8a6420;
    --gold-light: #f3d98a;
    --ruby: #b3122b;
    --ink-light: #f2f2f2;
    --ink-dark: #111111;
  }
  * { margin: 0; padding: 0; box-sizing: border-box; }
  html, body { width: 1200px; height: 1200px; overflow: hidden; }
  body {
    background: linear-gradient(180deg, var(--canvas-top) 0%, #e6e6e6 45%, var(--canvas-bottom) 100%);
    font-family: 'Tinos', 'Times New Roman', serif;
  }
  .label-row {
    position: absolute;
    top: 330px;
    left: 60px;
    display: flex;
    gap: 60px;
  }
  .label {
    position: relative;
    width: 320px;
    height: 520px;
    overflow: hidden;
    border-radius: 160px 6px 6px 6px / 60px 6px 6px 6px;
    display: flex;
    flex-direction: column;
    align-items: center;
  }
  .label--black { background: var(--label-black); color: var(--ink-light); }
  .label--white { background: var(--label-white); color: var(--ink-dark); box-shadow: 0 0 0 1px #dcdcdc; }

  .monogram-area {
    position: absolute;
    top: 24px;
    left: 30px;
    width: 260px;
    height: 180px;
    border-radius: 4px;
  }
  .label--black .monogram-area {
    background: radial-gradient(ellipse at 40% 50%, rgba(201,160,74,0.35) 0%, rgba(138,100,32,0.18) 55%, rgba(5,5,5,0) 100%);
  }
  .label--white .monogram-area {
    background: radial-gradient(ellipse at 40% 50%, rgba(201,160,74,0.30) 0%, rgba(243,217,138,0.18) 55%, rgba(255,255,255,0) 100%);
  }
  .karat {
    position: absolute;
    top: 212px;
    right: 44px;
    font-size: 28px;
    color: var(--ruby);
  }
  .brand-name {
    margin-top: 248px;
    font-family: 'Cinzel', serif;
    font-weight: 700;
    font-size: 31px;
    letter-spacing: 2px;
    color: var(--gold);
  }
  .tagline {
    margin-top: 2px;
    font-family: 'Pinyon Script', cursive;
    font-size: 19px;
    color: inherit;
  }
  .divider {
    width: 200px;
    height: 1px;
    margin-top: 6px;
    background: currentColor;
  }
  .product-type {
    margin-top: 8px;
    font-size: 24px;
    letter-spacing: 3px;
  }
  .process {
    margin-top: 10px;
    font-size: 15px;
    font-weight: 700;
    letter-spacing: 1px;
    display: flex;
    align-items: baseline;
    gap: 10px;
  }
  .process__count { font-size: 28px; font-weight: 400; color: var(--ruby); }
  .info-band {
    position: relative;
    z-index: 1;
    margin-top: 4px;
    width: 292px;
    padding: 2px 8px 4px;
    font-size: 12px;
    font-weight: 700;
    text-align: center;
  }
  .label--black .info-band {
    background: linear-gradient(90deg, var(--gold-dark), var(--gold-light) 35%, var(--gold) 60%, var(--gold-dark));
    color: var(--ink-dark);
  }
  .label--white .info-band { background: var(--label-black); color: var(--ink-light); }
  .info-band__row {
    display: flex;
    justify-content: space-between;
    margin-top: 3px;
    font-weight: 400;
  }
  .gold-sparkle {
    position: absolute;
    left: 0;
    bottom: 0;
    width: 100%;
    height: 68px;
    background: linear-gradient(180deg, rgba(201,160,74,0.25) 0%, var(--gold) 45%, var(--gold-dark) 100%);
  }
  .label--white .gold-sparkle {
    background: linear-gradient(180deg, rgba(201,160,74,0.15) 0%, #d9b968 50%, var(--gold-dark) 100%);
  }
</style>
</head>
<body>
  <main class="label-row">
    <section class="label label--black">
      <div class="monogram-area" role="img" aria-label="Brand monogram mark in gold"></div>
      <span class="karat">24 kt</span>
      <h1 class="brand-name">CORVELLE</h1>
      <p class="tagline">Premium Gold Sparkling</p>
      <span class="divider"></span>
      <h2 class="product-type">VODKA</h2>
      <p class="process">Distilled <span class="process__count">8</span> Filtered</p>
      <div class="info-band">
        Made In Germany
        <div class="info-band__row"><span>40% Alc/Vol</span><span>200ml</span><span>80 Proof</span></div>
      </div>
      <div class="gold-sparkle" role="img" aria-label="Scattered gold glitter flakes"></div>
    </section>

    <section class="label label--black">
      <div class="monogram-area" role="img" aria-label="Brand monogram mark in gold"></div>
      <span class="karat">24 kt</span>
      <h1 class="brand-name">CORVELLE</h1>
      <p class="tagline">Premium Gold Sparkling</p>
      <span class="divider"></span>
      <h2 class="product-type">VODKA</h2>
      <p class="process">Distilled <span class="process__count">8</span> Filtered</p>
      <div class="info-band">
        Made In Germany
        <div class="info-band__row"><span>40% Alc/Vol</span><span>200ml</span><span>80 Proof</span></div>
      </div>
      <div class="gold-sparkle" role="img" aria-label="Scattered gold glitter flakes"></div>
    </section>

    <section class="label label--white">
      <div class="monogram-area" role="img" aria-label="Brand monogram mark in gold"></div>
      <span class="karat">24 kt</span>
      <h1 class="brand-name">CORVELLE</h1>
      <p class="tagline">Premium Gold Sparkling</p>
      <span class="divider"></span>
      <h2 class="product-type">VODKA</h2>
      <p class="process">Distilled <span class="process__count">8</span> Filtered</p>
      <div class="info-band">
        Made In Germany
        <div class="info-band__row"><span>40% Alc/Vol</span><span>200ml</span><span>80 Proof</span></div>
      </div>
      <div class="gold-sparkle" role="img" aria-label="Scattered gold glitter flakes"></div>
    </section>
  </main>
</body>
</html>
```